GKL Auto - help to get me noticed

We not long ago tasked Pixel Harbor to design a logo for my business. I'm happy with the result so would like to have a business card designed as a follow up.

It's an Automotive service and repair business that offers the following -
- Servicing
- General repairs
- Brakes
- Detailing
- Integrity

GKL Automotive
Malcolm Pryde
0491 726 183

Target Market(s)

Everyday people with the ability to reach out to corporate customers also.

Industry/Entity Type

Automotive

Contact Information for Business Card

Black card, logo, name and phone number on front. Other details on back of card.

```html
<!DOCTYPE html>
<html lang="en">
<head>
<meta charset="utf-8">
<title>GKL Automotive – Business Card</title>
<link href="https://fonts.googleapis.com/css2?family=Arimo:wght@400;700&display=swap" rel="stylesheet">
<style>
  :root {
    --page: #2a2624;
    --card: #0b0b0b;
    --card-edge: #151515;
    --green: #8cc421;
    --green-light: #a6d22a;
    --green-dark: #5fa520;
    --white: #ffffff;
    --rule: #6a6a6a;
  }
  * { margin: 0; padding: 0; box-sizing: border-box; }
  html, body {
    width: 1200px; height: 842px; overflow: hidden;
    background: var(--page);
    font-family: "Arimo", Arial, sans-serif;
  }
  .canvas {
    position: relative; width: 1200px; height: 842px;
    display: flex; align-items: center; justify-content: center; gap: 60px;
  }
  .card {
    position: relative; width: 520px; height: 297px;
    background: linear-gradient(160deg, var(--card-edge), var(--card));
    overflow: hidden;
    box-shadow: 0 10px 30px rgba(0,0,0,.5);
  }

  /* Back: contact details */
  .band {
    position: absolute; left: 0; right: 0; height: 11px;
    background: linear-gradient(180deg, var(--green-light), var(--green-dark));
  }
  .band--top { top: 0; }
  .band--bottom { bottom: 0; }
  .contact {
    position: absolute; inset: 0;
    display: flex; flex-direction: column; align-items: center; justify-content: center;
  }
  .contact__name {
    color: var(--green); font-weight: 700; font-size: 27px; letter-spacing: .5px;
  }
  .contact__icons {
    display: flex; align-items: center; gap: 6px; margin: 10px 0 8px;
  }
  .contact__rule { width: 70px; height: 1px; background: var(--rule); margin: 0 8px; }
  .icon {
    width: 32px; height: 32px; border-radius: 6px;
    background: linear-gradient(180deg, var(--green-light), var(--green-dark));
    display: flex; align-items: center; justify-content: center;
  }
  .icon svg { width: 20px; height: 20px; }
  .contact__line { color: var(--white); font-size: 20px; line-height: 1.3; }

  /* Front: wordmark and services */
  .tab {
    position: absolute; width: 40px; height: 48px;
    background: linear-gradient(180deg, var(--green-light), var(--green-dark));
  }
  .tab::after {
    content: ""; position: absolute; top: 0; bottom: 0; width: 4px; background: var(--white);
  }
  .tab--left { left: 0; top: 152px; }
  .tab--left::after { right: 0; }
  .tab--right { right: 0; top: 40px; }
  .tab--right::after { left: 0; }
  .brand {
    position: absolute; left: 60px; right: 60px; top: 92px; text-align: center;
  }
  .brand__name {
    color: var(--green); font-weight: 700; font-size: 38px; letter-spacing: 1px;
    line-height: 1.1; text-transform: uppercase; white-space: nowrap;
  }
  .services {
    position: absolute; left: 0; right: 0; bottom: 56px;
    display: flex; justify-content: center; align-items: center;
    color: var(--white); font-size: 15px;
  }
  .services__dot {
    width: 7px; height: 7px; border-radius: 50%; background: var(--green); margin: 0 5px;
  }
</style>
</head>
<body>
<main class="canvas">
  <section class="card card--back">
    <div class="band band--top"></div>
    <div class="contact">
      <h1 class="contact__name">MALCOLM PRYDE</h1>
      <div class="contact__icons">
        <span class="contact__rule"></span>
        <span class="icon" aria-label="Phone">
          <svg viewBox="0 0 20 20" fill="none" stroke="#0b0b0b" stroke-width="1.6">
            <path d="M3 8c0-3 14-3 14 0v1h-3V7H6v2H3z" fill="#0b0b0b"/>
            <rect x="5" y="10" width="10" height="6" rx="1"/>
          </svg>
        </span>
        <span class="icon" aria-label="Email">
          <svg viewBox="0 0 20 20" fill="none" stroke="#0b0b0b" stroke-width="1.6">
            <rect x="3" y="5" width="14" height="10"/>
            <path d="M3 5l7 6 7-6M3 15l5-5M17 15l-5-5"/>
          </svg>
        </span>
        <span class="icon" aria-label="Website">
          <svg viewBox="0 0 20 20" fill="none" stroke="#0b0b0b" stroke-width="1.6">
            <circle cx="10" cy="10" r="7"/>
            <ellipse cx="10" cy="10" rx="3" ry="7"/>
            <path d="M3 10h14"/>
          </svg>
        </span>
        <span class="contact__rule"></span>
      </div>
      <p class="contact__line">0491 726 183</p>
      <p class="contact__line">info@gklautomotive.com</p>
      <p class="contact__line">www.gklautomotive.com</p>
    </div>
    <div class="band band--bottom"></div>
  </section>

  <section class="card card--front">
    <div class="tab tab--left"></div>
    <div class="tab tab--right"></div>
    <div class="brand">
      <p class="brand__name">GKL Automotive</p>
    </div>
    <p class="services">
      <span>Servicing</span><span class="services__dot"></span>
      <span>General repairs</span><span class="services__dot"></span>
      <span>Brakes</span><span class="services__dot"></span>
      <span>Detailing</span><span class="services__dot"></span>
      <span>Integrity</span>
    </p>
  </section>
</main>
</body>
</html>
```